AUSTRALIA SUPPLEMENT - Protein label design - CREATIVE, FEMININE, UNIQUE

I need help with the design of what will be my line of supplements. (Protein, plant base, collagen , BCAAs, etc)
I'm starting off with protein isolate - with the flavours VANILLA, CHOCOLATE, BOYSENBERRY, HONEYCOMB.
I need help with the design of what the product will look like for my range.
(Great opportunity for further work)

Looking for a unique, elegant, stand out, feminine design, some slight sparkle or something that stands out on a shelf.
With symbols to represent what's in it, raised text. with some quirky cute things on it. (not sure what) Something that captured young womens eyes and easy to understand. things on it that appeals to women such as
LOW CALORIE, GREAT TASTING, GLUTEN FREE, 100 NATURAL, NATURALLY SWEETENED, HIGH PROTEIN.etc and whatever you can think of (open to ideas) but within KMO guidelines.

Mostly just after the look and creativity of what the front will look like. Don't have to worry about the back area.

My market will be for females aged 18-35

I have a activewear line called DORUMEN which will go with this. which I will attach the logo below amongst some other things that match my packaging. (again open to ideas)

I have attached a label of what one will look like( EXAMPLE).
. Among others that look nice But again I want to be different, unique to stand out. I don't want it to look like these. it's just the only ones I found online I liked that suit my market.

Feel free to ask any questions! :)
Updates

Extending time as I want this to be to be what will be on the shelves of many stores. I know that needs time to be able to do a quality job.

Target Market(s)

18-35

Industry/Entity Type

Supplement

Font styles to use
Serif
Script

Colors
f9d9e8
ffffff
fbd3d4
ecf7fb
e4daeb
cfeae6
eea4c8
fdfad7
f59195

Requirements
Must have
• Word - DORUMEN
PROTEIN ISOLATE
FLAVOUR
SYMBOLS

Looking for a unique, elegant, stand out, colour, feminine design, some slight sparkle or something that stands out on a shelf.

IT WILL BE ON A WHITE TUB or CLEAR - Perhaps detail on the lid
Nice to have
• Looking for a unique, elegant, stand out, colour, feminine design, some slight sparkle or something that stands out on a shelf. Something artsy.

will be on a white or clear tub with a white label background (possibly)
Should not have
• I don’t want it dark looking.
Something bright, vibrant, whites, pinks, sparkles (maybe) colours.

I don't want the word activewear on it.

```html
<!DOCTYPE html>
<html lang="en">
<head>
<meta charset="utf-8">
<title>Protein Isolate Label Range</title>
<link href="https://fonts.googleapis.com/css2?family=Playfair+Display:wght@400&family=Montserrat:ital,wght@1,900&family=Dancing+Script:wght@500&family=Open+Sans:wght@400;600&family=Oswald:wght@500&display=swap" rel="stylesheet">
<style>
  :root{
    --ink:#1d1d1d;
    --rule:#555;
    --pink:#e4147a;
    --teal:#1a9e94;
    --barcode-blue:#1a95d8;
    --wash-pink:#f3e6ea;
    --wash-grey:#eeedef;
  }
  html,body{margin:0;padding:0;overflow:hidden;background:#fff;}
  .canvas{position:relative;width:1045px;height:1200px;background:#fff;font-family:"Open Sans",sans-serif;color:var(--ink);}

  .dim-width{position:absolute;left:157px;width:759px;height:40px;}
  .dim-width .value{position:absolute;top:-14px;left:0;width:100%;text-align:center;font-size:17px;}
  .dim-width .line{position:absolute;top:19px;left:0;width:100%;border-top:1px solid var(--rule);}
  .dim-width .tick{position:absolute;top:0;height:40px;border-left:1px solid var(--rule);}
  .dim-width .tick.start{left:0}.dim-width .tick.end{right:0}

  .dim-height{position:absolute;left:87px;width:41px;height:254px;}
  .dim-height .line{position:absolute;left:20px;top:0;height:100%;border-left:1px solid var(--rule);}
  .dim-height .tick{position:absolute;left:0;width:41px;border-top:1px solid var(--rule);}
  .dim-height .tick.start{top:0}.dim-height .tick.end{bottom:0}
  .dim-height .value{position:absolute;left:-49px;top:117px;width:100px;text-align:center;font-size:17px;transform:rotate(-90deg);}

  .label{position:absolute;left:157px;width:759px;height:254px;border:1px solid #9a9a9a;box-sizing:border-box;overflow:hidden;background:#fff;}
  .label.vanilla{--band-dark:#cfa475;--band-mid:#e5cbb0;--band-light:#efe3d6;--flavour:#c49a66;}
  .label.boysenberry{--band-dark:#e2004c;--band-mid:#f0939d;--band-light:#f7c3ca;--flavour:#e2004c;}
  .label.honeycomb{--band-dark:#c46c1a;--band-mid:#e5b386;--band-light:#f3d4b8;--flavour:#c46c1a;}

  .artwork{position:absolute;top:0;height:208px;width:276px;}
  .artwork.left{left:0;background:linear-gradient(90deg,var(--wash-grey),#fff 55%,var(--wash-pink));}
  .artwork.right{left:483px;background:linear-gradient(90deg,var(--wash-grey),#fbf8f9 50%,var(--wash-pink));}

  .band{position:absolute;top:208px;width:276px;height:46px;}
  .band.left{left:0}.band.right{left:483px}
  .band svg{display:block;width:100%;height:100%}
  .band .dark{fill:var(--band-dark)}.band .mid{fill:var(--band-mid)}.band .light{fill:var(--band-light)}

  .nutrition{position:absolute;left:63px;top:19px;width:105px;height:196px;background:#fff;padding:3px 5px;box-sizing:border-box;font-size:3.1px;line-height:3.9px;}
  .nutrition .serving{font-weight:600;font-size:3.3px;border-bottom:1.2px solid var(--ink);padding-bottom:1px;}
  .nutrition table{width:100%;border-collapse:collapse;}
  .nutrition td{padding:0;border-bottom:.3px solid #999;}
  .nutrition .head td{font-weight:600;font-size:2.4px;line-height:2.6px;border-bottom:1px solid var(--ink);}
  .nutrition .breakdown{display:flex;gap:3px;margin-top:3px;}
  .nutrition .breakdown > div{flex:1}
  .nutrition .sub{font-weight:600;font-size:2.4px;border-bottom:.5px solid var(--ink);}
  .nutrition .note{font-size:2.2px;line-height:2.6px;}
  .nutrition .ingredients{margin-top:3px;border-top:.5px solid var(--ink);padding-top:2px;font-size:3px;line-height:4.8px;}

  .brand{position:absolute;left:292px;top:40px;width:150px;font-family:"Playfair Display",serif;font-size:29px;letter-spacing:2px;color:var(--ink);}
  .title{position:absolute;font-family:"Montserrat",sans-serif;font-weight:900;font-style:italic;font-size:36px;color:var(--pink);text-shadow:2px 2px 2px rgba(0,0,0,.35);transform:rotate(-8deg);white-space:nowrap;}
  .title.protein{left:300px;top:79px;}
  .title.isolate{left:292px;top:126px;}
  .flavour{position:absolute;top:163px;font-family:"Dancing Script",cursive;font-size:32px;color:var(--flavour);white-space:nowrap;}
  .vanilla .flavour{left:366px}
  .boysenberry .flavour{left:336px}
  .honeycomb .flavour{left:340px}

  .claims{position:absolute;left:296px;top:218px;display:flex;gap:6px;}
  .claim{width:37px;text-align:center;font-family:"Oswald",sans-serif;font-size:4.6px;color:var(--teal);}
  .claim svg{display:block;width:35px;height:25px;margin:0 auto 1px;}
  .claim .badge{fill:none;stroke:var(--teal);stroke-width:1.8}
  .claim .mark{fill:var(--teal)}
  .low-cal{position:absolute;left:420px;top:218px;width:34px;height:24px;background:var(--pink);border-radius:4px 12px 4px 12px;color:#fff;font-family:"Oswald",sans-serif;text-align:center;font-size:5.4px;line-height:8px;padding-top:3px;box-sizing:border-box;}
  .low-cal .low{display:block;background:#fff;color:var(--pink);width:17px;margin:0 auto;line-height:7px;border-radius:2px;}

  .origin-badge{position:absolute;left:608px;top:170px;width:33px;height:32px;background:#fff;border:1px solid var(--ink);box-sizing:border-box;}
  .origin-badge span{position:absolute;left:8px;top:3px;width:16px;height:13px;background:var(--pink);border-radius:3px;}
  .barcode-box{position:absolute;left:655px;top:149px;width:94px;height:54px;background:#fff;border:1px solid #bfe3f3;box-sizing:border-box;display:flex;align-items:center;justify-content:center;color:var(--barcode-blue);font-size:10.5px;}
</style>
</head>
<body>
<div class="canvas">

  <!-- Vanilla -->
  <div class="dim-width" style="top:82px"><span class="value">282.84 mm</span><span class="line"></span><span class="tick start"></span><span class="tick end"></span></div>
  <div class="dim-height" style="top:132px"><span class="line"></span><span class="tick start"></span><span class="tick end"></span><span class="value">94.89 mm</span></div>
  <section class="label vanilla" style="top:132px">
    <div class="artwork left" role="img" aria-label="Watercolour leaf artwork in blush pink and grey"></div>
    <div class="artwork right" role="img" aria-label="Watercolour leaf artwork in blush pink, grey and lilac"></div>
    <div class="band left"><svg viewBox="0 0 276 46" preserveAspectRatio="none"><rect class="light" width="276" height="46"/><polygon class="mid" points="0,0 276,0 200,46 0,46"/><polygon class="dark" points="0,0 172,0 100,46 0,46"/></svg></div>
    <div class="band right"><svg viewBox="0 0 276 46" preserveAspectRatio="none"><rect class="light" width="276" height="46"/><polygon class="mid" points="0,0 256,0 180,46 0,46"/><polygon class="dark" points="0,0 180,0 98,46 0,46"/></svg></div>
    <div class="nutrition">
      <div class="serving">Serving Size: 30g (1 scoop) &nbsp;Serves per Container: 30</div>
      <table>
        <tr class="head"><td></td><td>Amount Per 30g</td><td>Amount Per 100g</td></tr>
        <tr><td>Energy</td><td>511kJ / 122Cal</td><td>1702kJ / 407Cal</td></tr>
        <tr><td>Protein</td><td>23.4g</td><td>78.0g</td></tr>
        <tr><td>Fat, total</td><td>2.1g</td><td>6.9g</td></tr>
        <tr><td>Saturated</td><td>2.1g</td><td>4.67g</td></tr>
        <tr><td>Carbohydrate, total</td><td>2.1g</td><td>7.1g</td></tr>
        <tr><td>&nbsp;- Sugars</td><td>1.1g</td><td>3.8g</td></tr>
      </table>
      <div class="breakdown">
        <div><div class="sub">AMINO ACID PROFILE per 100g</div>
          L-Leucine 8.61<br>L-Valine 4.92<br>L-Threonine 4.9<br>L-Phenylalanine 2.78<br>L-Arginine 2.4<br>L-Cysteine 1.36<br>L-Glutamic Acid 15.93<br>L-Histidine 1.63<br>L-Serine 4.66<br>L-Isoleucine 5.19<br>L-Lysine 6.13<br>L-Methionine 1.84<br>L-Tryptophan 1.3<br>L-Aspartic Acid 7.18<br>L-Alanine 3.79<br>L-Glycine 1.66<br>L-Proline 2.88<br>L-Tyrosine 2.84<br><span class="note">*Essential Amino Acids</span></div>
        <div><div class="sub">MULTIVITAMIN MINERAL per 30g</div>
          Vit A 2µg<br>B1 4µg · B2 5µg<br>B3 0.03mg · Folate 1µg<br>B6 5µg · B12 1µg<br>C 0.2mg · D 1µg<br>E 0.03mg · Calcium 3mg<br>Iodine 1µg · Iron 0.03mg<br>Phosphorus 3mg<br>Zinc 0.03mg · Biotin 1µg<br>B5 5µg · K 1µg<br>Chromium 1µg · Copper 3µg<br>Magnesium 5µg<br>Molybdenum 3µg<br>Selenium 1µg<br>Ashwagandha 100mg</div>
      </div>
      <div class="ingredients">Ingredients: Instantised Whey Protein Concentrate, 100% Instantised Hydrolysed Whey Protein Isolate, Soy Lecithin, Digestive Enzymes, Ashwagandha, Chromium, Vitamins, Sodium, Potassium, Calcium, Magnesium, Iron, Manganese, Copper, Stevia, Flavour.</div>
    </div>
    <div class="brand">DORUMEN</div>
    <div class="title protein">PROTEIN</div>
    <div class="title isolate">ISOLATE</div>
    <div class="flavour">Vanilla</div>
    <div class="claims">
      <div class="claim"><svg viewBox="0 0 35 25"><path class="badge" d="M4 3h27v12a10 10 0 0 1-10 9H4z"/><path class="mark" d="M10 18 L26 7 L24 12 Z"/></svg>GLUTEN FREE</div>
      <div class="claim"><svg viewBox="0 0 35 25"><path class="badge" d="M4 3h27v12a10 10 0 0 1-10 9H4z"/><circle class="mark" cx="17.5" cy="9" r="3"/><rect class="mark" x="10" y="13" width="15" height="7" rx="3"/></svg>HIGH IN PROTEIN</div>
      <div class="claim"><svg viewBox="0 0 35 25"><path class="badge" d="M4 3h27v12a10 10 0 0 1-10 9H4z"/><path class="mark" d="M9 20 C9 10 18 6 27 6 C26 15 20 20 9 20Z"/></svg>100% NATURAL</div>
    </div>
    <div class="low-cal"><span class="low">LOW</span>CALORIE</div>
    <div class="origin-badge" role="img" aria-label="Origin badge"><span></span></div>
    <div class="barcode-box">Barcode</div>
  </section>

  <!-- Boysenberry -->
  <div class="dim-width" style="top:433px;left:158px"><span class="value">282.84 mm</span><span class="line"></span><span class="tick start"></span><span class="tick end"></span></div>
  <div class="dim-height" style="top:483px;left:88px"><span class="line"></span><span class="tick start"></span><span class="tick end"></span><span class="value">94.89 mm</span></div>
  <section class="label boysenberry" style="top:483px;left:158px">
    <div class="artwork left" role="img" aria-label="Watercolour leaf artwork in blush pink and grey"></div>
    <div class="artwork right" role="img" aria-label="Watercolour leaf artwork in blush pink, grey and lilac"></div>
    <div class="band left"><svg viewBox="0 0 276 46" preserveAspectRatio="none"><rect class="light" width="276" height="46"/><polygon class="mid" points="0,0 276,0 200,46 0,46"/><polygon class="dark" points="0,0 172,0 100,46 0,46"/></svg></div>
    <div class="band right"><svg viewBox="0 0 276 46" preserveAspectRatio="none"><rect class="light" width="276" height="46"/><polygon class="mid" points="0,0 256,0 180,46 0,46"/><polygon class="dark" points="0,0 180,0 98,46 0,46"/></svg></div>
    <div class="nutrition">
      <div class="serving">Serving Size: 30g (1 scoop) &nbsp;Serves per Container: 30</div>
      <table>
        <tr class="head"><td></td><td>Amount Per 30g</td><td>Amount Per 100g</td></tr>
        <tr><td>Energy</td><td>511kJ / 122Cal</td><td>1702kJ / 407Cal</td></tr>
        <tr><td>Protein</td><td>23.4g</td><td>78.0g</td></tr>
        <tr><td>Fat, total</td><td>2.1g</td><td>6.9g</td></tr>
        <tr><td>Saturated</td><td>2.1g</td><td>4.67g</td></tr>
        <tr><td>Carbohydrate, total</td><td>2.1g</td><td>7.1g</td></tr>
        <tr><td>&nbsp;- Sugars</td><td>1.1g</td><td>3.8g</td></tr>
      </table>
      <div class="breakdown">
        <div><div class="sub">AMINO ACID PROFILE per 100g</div>
          L-Leucine 8.61<br>L-Valine 4.92<br>L-Threonine 4.9<br>L-Phenylalanine 2.78<br>L-Arginine 2.4<br>L-Cysteine 1.36<br>L-Glutamic Acid 15.93<br>L-Histidine 1.63<br>L-Serine 4.66<br>L-Isoleucine 5.19<br>L-Lysine 6.13<br>L-Methionine 1.84<br>L-Tryptophan 1.3<br>L-Aspartic Acid 7.18<br>L-Alanine 3.79<br>L-Glycine 1.66<br>L-Proline 2.88<br>L-Tyrosine 2.84<br><span class="note">*Essential Amino Acids</span></div>
        <div><div class="sub">MULTIVITAMIN MINERAL per 30g</div>
          Vit A 2µg<br>B1 4µg · B2 5µg<br>B3 0.03mg · Folate 1µg<br>B6 5µg · B12 1µg<br>C 0.2mg · D 1µg<br>E 0.03mg · Calcium 3mg<br>Iodine 1µg · Iron 0.03mg<br>Phosphorus 3mg<br>Zinc 0.03mg · Biotin 1µg<br>B5 5µg · K 1µg<br>Chromium 1µg · Copper 3µg<br>Magnesium 5µg<br>Molybdenum 3µg<br>Selenium 1µg<br>Ashwagandha 100mg</div>
      </div>
      <div class="ingredients">Ingredients: Instantised Whey Protein Concentrate, 100% Instantised Hydrolysed Whey Protein Isolate, Soy Lecithin, Digestive Enzymes, Ashwagandha, Chromium, Vitamins, Sodium, Potassium, Calcium, Magnesium, Iron, Manganese, Copper, Stevia, Flavour.</div>
    </div>
    <div class="brand">DORUMEN</div>
    <div class="title protein">PROTEIN</div>
    <div class="title isolate">ISOLATE</div>
    <div class="flavour">Boysenberry</div>
    <div class="claims">
      <div class="claim"><svg viewBox="0 0 35 25"><path class="badge" d="M4 3h27v12a10 10 0 0 1-10 9H4z"/><path class="mark" d="M10 18 L26 7 L24 12 Z"/></svg>GLUTEN FREE</div>
      <div class="claim"><svg viewBox="0 0 35 25"><path class="badge" d="M4 3h27v12a10 10 0 0 1-10 9H4z"/><circle class="mark" cx="17.5" cy="9" r="3"/><rect class="mark" x="10" y="13" width="15" height="7" rx="3"/></svg>HIGH IN PROTEIN</div>
      <div class="claim"><svg viewBox="0 0 35 25"><path class="badge" d="M4 3h27v12a10 10 0 0 1-10 9H4z"/><path class="mark" d="M9 20 C9 10 18 6 27 6 C26 15 20 20 9 20Z"/></svg>100% NATURAL</div>
    </div>
    <div class="low-cal"><span class="low">LOW</span>CALORIE</div>
    <div class="origin-badge" role="img" aria-label="Origin badge"><span></span></div>
    <div class="barcode-box">Barcode</div>
  </section>

  <!-- Honeycomb -->
  <div class="dim-width" style="top:816px"><span class="value">282.84 mm</span><span class="line"></span><span class="tick start"></span><span class="tick end"></span></div>
  <div class="dim-height" style="top:866px"><span class="line"></span><span class="tick start"></span><span class="tick end"></span><span class="value">94.89 mm</span></div>
  <section class="label honeycomb" style="top:866px">
    <div class="artwork left" role="img" aria-label="Watercolour leaf artwork in blush pink and grey"></div>
    <div class="artwork right" role="img" aria-label="Watercolour leaf artwork in blush pink, grey and lilac"></div>
    <div class="band left"><svg viewBox="0 0 276 46" preserveAspectRatio="none"><rect class="light" width="276" height="46"/><polygon class="mid" points="0,0 276,0 200,46 0,46"/><polygon class="dark" points="0,0 172,0 100,46 0,46"/></svg></div>
    <div class="band right"><svg viewBox="0 0 276 46" preserveAspectRatio="none"><rect class="light" width="276" height="46"/><polygon class="mid" points="0,0 256,0 180,46 0,46"/><polygon class="dark" points="0,0 180,0 98,46 0,46"/></svg></div>
    <div class="nutrition">
      <div class="serving">Serving Size: 30g (1 scoop) &nbsp;Serves per Container: 30</div>
      <table>
        <tr class="head"><td></td><td>Amount Per 30g</td><td>Amount Per 100g</td></tr>
        <tr><td>Energy</td><td>511kJ / 122Cal</td><td>1702kJ / 407Cal</td></tr>
        <tr><td>Protein</td><td>23.4g</td><td>78.0g</td></tr>
        <tr><td>Fat, total</td><td>2.1g</td><td>6.9g</td></tr>
        <tr><td>Saturated</td><td>2.1g</td><td>4.67g</td></tr>
        <tr><td>Carbohydrate, total</td><td>2.1g</td><td>7.1g</td></tr>
        <tr><td>&nbsp;- Sugars</td><td>1.1g</td><td>3.8g</td></tr>
      </table>
      <div class="breakdown">
        <div><div class="sub">AMINO ACID PROFILE per 100g</div>
          L-Leucine 8.61<br>L-Valine 4.92<br>L-Threonine 4.9<br>L-Phenylalanine 2.78<br>L-Arginine 2.4<br>L-Cysteine 1.36<br>L-Glutamic Acid 15.93<br>L-Histidine 1.63<br>L-Serine 4.66<br>L-Isoleucine 5.19<br>L-Lysine 6.13<br>L-Methionine 1.84<br>L-Tryptophan 1.3<br>L-Aspartic Acid 7.18<br>L-Alanine 3.79<br>L-Glycine 1.66<br>L-Proline 2.88<br>L-Tyrosine 2.84<br><span class="note">*Essential Amino Acids</span></div>
        <div><div class="sub">MULTIVITAMIN MINERAL per 30g</div>
          Vit A 2µg<br>B1 4µg · B2 5µg<br>B3 0.03mg · Folate 1µg<br>B6 5µg · B12 1µg<br>C 0.2mg · D 1µg<br>E 0.03mg · Calcium 3mg<br>Iodine 1µg · Iron 0.03mg<br>Phosphorus 3mg<br>Zinc 0.03mg · Biotin 1µg<br>B5 5µg · K 1µg<br>Chromium 1µg · Copper 3µg<br>Magnesium 5µg<br>Molybdenum 3µg<br>Selenium 1µg<br>Ashwagandha 100mg</div>
      </div>
      <div class="ingredients">Ingredients: Instantised Whey Protein Concentrate, 100% Instantised Hydrolysed Whey Protein Isolate, Soy Lecithin, Digestive Enzymes, Ashwagandha, Chromium, Vitamins, Sodium, Potassium, Calcium, Magnesium, Iron, Manganese, Copper, Stevia, Flavour.</div>
    </div>
    <div class="brand">DORUMEN</div>
    <div class="title protein">PROTEIN</div>
    <div class="title isolate">ISOLATE</div>
    <div class="flavour">Honeycomb</div>
    <div class="claims">
      <div class="claim"><svg viewBox="0 0 35 25"><path class="badge" d="M4 3h27v12a10 10 0 0 1-10 9H4z"/><path class="mark" d="M10 18 L26 7 L24 12 Z"/></svg>GLUTEN FREE</div>
      <div class="claim"><svg viewBox="0 0 35 25"><path class="badge" d="M4 3h27v12a10 10 0 0 1-10 9H4z"/><circle class="mark" cx="17.5" cy="9" r="3"/><rect class="mark" x="10" y="13" width="15" height="7" rx="3"/></svg>HIGH IN PROTEIN</div>
      <div class="claim"><svg viewBox="0 0 35 25"><path class="badge" d="M4 3h27v12a10 10 0 0 1-10 9H4z"/><path class="mark" d="M9 20 C9 10 18 6 27 6 C26 15 20 20 9 20Z"/></svg>100% NATURAL</div>
    </div>
    <div class="low-cal"><span class="low">LOW</span>CALORIE</div>
    <div class="origin-badge" role="img" aria-label="Origin badge"><span></span></div>
    <div class="barcode-box">Barcode</div>
  </section>

</div>
</body>
</html>
```